Stationery Design Project

KT7 Staffing requires letterhead and business card designs for a company based in London. Just like the name, we're a management resourcing company, providing resources to third party companies. You can see www.kt7staffing-example.com for ideas on existing colour schemes and design concepts that have been implimented and agreed to. Ultimately the design should broadcast professionalism, safety and the concept of growth.

Target Market(s)

Financial institutes; friendly societies (All UK based)

Industry/Entity Type

Safety

Requirements
Must have
• Files produced should be print ready; and the text in them editable (eg address, name etc)

```html
<!DOCTYPE html>
<html lang="en">
<head>
<meta charset="utf-8">
<title>KT7 Staffing — Business Card</title>
<link rel="stylesheet" href="https://fonts.googleapis.com/css2?family=Arimo:wght@400;700&display=swap">
<style>
  :root {
    --page-bg: #ffffff;
    --card-dark: #2f3a42;
    --card-mid: #3b4a53;
    --card-light: #455660;
    --brand-teal: #2f8e90;
    --tab-grey: #cfcfcf;
  }
  html, body {
    margin: 0;
    padding: 0;
    width: 1200px;
    height: 831px;
    overflow: hidden;
    background: var(--page-bg);
  }
  .canvas {
    position: relative;
    width: 1200px;
    height: 831px;
  }
  .business-card {
    position: absolute;
    left: 150px;
    top: 171px;
    width: 900px;
    height: 489px;
    background: linear-gradient(160deg, var(--card-dark) 0%, var(--card-mid) 55%, var(--card-light) 100%);
    clip-path: polygon(40px 0, 100% 0, 100% 100%, 0 100%, 0 40px);
    font-family: "Arimo", Arial, sans-serif;
  }
  .brand-lockup {
    position: absolute;
    left: 78px;
    top: 180px;
    display: flex;
    align-items: center;
    gap: 28px;
  }
  .brand-square {
    width: 56px;
    height: 56px;
    background: var(--brand-teal);
  }
  .brand-name {
    margin: 0;
    font-size: 96px;
    font-weight: 700;
    line-height: 1;
    letter-spacing: 1px;
    color: var(--brand-teal);
  }
  .corner-tab {
    position: absolute;
    right: 0;
    top: 418px;
    width: 194px;
    height: 47px;
    background: var(--tab-grey);
  }
</style>
</head>
<body>
  <main class="canvas">
    <section class="business-card" aria-label="KT7 Staffing business card, front">
      <div class="brand-lockup">
        <span class="brand-square" aria-hidden="true"></span>
        <h1 class="brand-name">KT7 Staffing</h1>
      </div>
      <div class="corner-tab" aria-hidden="true"></div>
    </section>
  </main>
</body>
</html>
```